French for French

Cover for the book "The Plume Vagabonde" ("How to write in French"). The book seeks to teach English to English: words, grammar, syntax. The lessons are pleasant, the style is very classical.

Target Market(s)

Middle class interested in improving her language.

Industry/Entity Type

Publishing Company

Colors

Designer to choose colors to be used in the design.

Requirements
Must have
• Author: "Bernard Morlaix" Title: "The Lively Pen" Publisher: "Quillon Editions" Size: 14 x 20,5 cm

```html
<!DOCTYPE html>
<html lang="fr">
<head>
<meta charset="utf-8">
<title>La Plume Vagabonde — Bernard Morlaix</title>
<link href="https://fonts.googleapis.com/css2?family=Anton&family=Chakra+Petch:wght@600&family=Roboto:wght@400&display=swap" rel="stylesheet">
<style>
  :root {
    --tricolor-red: #ec2a3c;
    --tricolor-blue: #022288;
    --paper: #ffffff;
    --sky-tint: #e8ecf7;
  }
  html, body {
    margin: 0;
    padding: 0;
    overflow: hidden;
    background: var(--paper);
  }
  .cover {
    position: relative;
    width: 820px;
    height: 1200px;
    background: var(--paper);
    overflow: hidden;
  }
  .author-band {
    position: absolute;
    inset: 0 0 auto 0;
    height: 132px;
    background: var(--tricolor-red);
  }
  .author-band svg,
  .book-title,
  .publisher {
    position: absolute;
    left: 0;
    width: 820px;
  }
  .author-band svg { top: 0; height: 132px; }
  .author-name {
    font-family: "Chakra Petch", sans-serif;
    font-weight: 600;
    font-size: 52px;
    fill: var(--paper);
  }
  .book-title { top: 190px; height: 360px; }
  .title-line {
    font-family: "Anton", sans-serif;
    font-size: 168px;
    fill: var(--tricolor-blue);
  }
  .paris-scene {
    position: absolute;
    left: 0;
    top: 586px;
    width: 820px;
    height: 511px;
    background: linear-gradient(180deg,
      var(--paper) 0%,
      var(--sky-tint) 30%,
      var(--tricolor-blue) 62%,
      var(--tricolor-blue) 78%,
      var(--tricolor-red) 100%);
  }
  .publisher { top: 1110px; height: 70px; }
  .publisher-name {
    font-family: "Roboto", sans-serif;
    font-size: 52px;
    fill: var(--tricolor-blue);
  }
</style>
</head>
<body>
<main class="cover">
  <header class="author-band">
    <svg viewBox="0 0 820 132" aria-label="Bernard Morlaix">
      <text class="author-name" x="134" y="92" textLength="554" lengthAdjust="spacing">BERNARD MORLAIX</text>
    </svg>
  </header>

  <svg class="book-title" viewBox="0 0 820 360" role="heading" aria-level="1" aria-label="La Plume Vagabonde">
    <text class="title-line" x="76" y="148" textLength="668" lengthAdjust="spacingAndGlyphs">LA PLUME</text>
    <text class="title-line" x="68" y="340" textLength="684" lengthAdjust="spacingAndGlyphs">VAGABONDE</text>
  </svg>

  <div class="paris-scene" role="img" aria-label="Silhouette of the Paris skyline in blue and red with the Eiffel Tower, a windmill and domes, above a tricolour river"></div>

  <footer>
    <svg class="publisher" viewBox="0 0 820 70" aria-label="Editions Quillon">
      <text class="publisher-name" x="128" y="56" textLength="566" lengthAdjust="spacing">EDITIONS QUILLON</text>
    </svg>
  </footer>
</main>
</body>
</html>
```